Dale Harwick Realtors
Stationary, Letterhead, Business Cards & Envelopes
Modern
Dale Harwick
Broker/ Owner
5817 Elmwood Crest Rd.
Fort Worth, Texas 76243
daleharwick@vesnamail.net
www.DaleHarwickRealtors.com
I would like the back to be the logo and I am not sure if it should have a white background or some color, I am open.
use logo here

```html
<!DOCTYPE html>
<html lang="en">
<head>
<meta charset="utf-8">
<title>Dale Harwick Realtors – Business Cards</title>
<link rel="stylesheet" href="https://fonts.googleapis.com/css2?family=Cinzel:wght@400;600&family=Montserrat:wght@400;500&display=swap">
<style>
  :root {
    --backdrop: #e9e6e1;
    --navy-deep: #0d1a4a;
    --navy: #1c2f7a;
    --royal: #2a46a8;
    --charcoal: #151515;
    --graphite: #3a3a3c;
    --paper: #ffffff;
    --ink: #1e2a5e;
    --ink-soft: #3b3f4e;
    --white: #ffffff;
    --silver: #cfd3dc;
  }
  * { box-sizing: border-box; margin: 0; padding: 0; }
  html, body { width: 1200px; height: 742px; overflow: hidden; }
  body { background: var(--backdrop); position: relative; font-family: "Montserrat", sans-serif; }

  .card {
    position: absolute; width: 530px; height: 295px; border-radius: 16px;
    overflow: hidden; box-shadow: 0 6px 16px rgba(0,0,0,.28);
  }
  .card--front { left: 50px; top: 68px; background: var(--paper); }
  .card--back-blue { left: 615px; top: 68px; background: radial-gradient(ellipse at 30% 40%, var(--royal), var(--navy) 55%, var(--navy-deep)); }
  .card--back-dark { left: 50px; top: 386px; background: linear-gradient(135deg, var(--charcoal) 10%, var(--graphite) 55%, #202022); }
  .card--back-navy { left: 615px; top: 386px; background: radial-gradient(ellipse at 30% 30%, var(--royal), var(--navy) 55%, var(--navy-deep)); }

  .card__wave { position: absolute; left: 0; top: 0; width: 530px; height: 110px; }

  .holder { position: absolute; left: 26px; top: 16px; color: var(--white); }
  .holder__name { font-family: "Cinzel", serif; font-size: 19px; font-weight: 400; letter-spacing: .5px; }
  .holder__role { font-size: 10px; margin-top: 2px; }
  .card__web-top { position: absolute; right: 28px; top: 16px; color: var(--white); font-size: 10px; }

  .wordmark {
    font-family: "Cinzel", serif; font-weight: 400; text-align: center;
    display: flex; align-items: center; justify-content: center; gap: 14px;
  }
  .wordmark__square { width: 22px; height: 22px; background: currentColor; }
  .card--front .wordmark { position: absolute; left: 0; right: 0; top: 132px; color: var(--ink); font-size: 32px; }

  .contacts { position: absolute; left: 0; right: 0; top: 228px; font-size: 10.5px; color: var(--ink-soft); text-align: center; }
  .contacts__row { display: flex; justify-content: center; gap: 16px; align-items: center; }
  .contacts__item { display: inline-flex; align-items: center; gap: 5px; }
  .contacts__item svg { width: 11px; height: 11px; fill: var(--royal); }
  .contacts__address { margin-top: 12px; }

  .card--back-blue .wordmark { position: absolute; left: 0; right: 0; top: 122px; color: var(--white); font-size: 36px; }
  .card--back-dark .wordmark, .card--back-navy .wordmark {
    position: absolute; left: 0; right: 0; top: 100px; color: var(--white); font-size: 34px;
  }
  .card--back-dark .wordmark { color: var(--silver); }
  .card__web-bottom {
    position: absolute; left: 0; right: 0; bottom: 38px; text-align: center;
    color: var(--white); font-size: 12px; letter-spacing: 3px;
  }
</style>
</head>
<body>

<section class="card card--front">
  <svg class="card__wave" viewBox="0 0 530 110" preserveAspectRatio="none">
    <defs>
      <linearGradient id="waveBlue" x1="0" y1="0" x2="1" y2="0">
        <stop offset="0" stop-color="#0d1a4a"/>
        <stop offset=".6" stop-color="#1c2f7a"/>
        <stop offset="1" stop-color="#2a46a8"/>
      </linearGradient>
    </defs>
    <path d="M0 0H530V34C420 30 330 46 250 74C170 100 80 104 0 86Z" fill="#121212" opacity=".85"/>
    <path d="M0 0H530V26C420 22 330 36 250 62C170 88 80 92 0 74Z" fill="url(#waveBlue)"/>
  </svg>
  <div class="holder">
    <div class="holder__name">Dale Harwick</div>
    <div class="holder__role">Broker/ Owner</div>
  </div>
  <div class="card__web-top">www.DaleHarwickRealtors.com</div>

  <div class="wordmark"><span class="wordmark__square"></span>Dale Harwick Realtors</div>

  <div class="contacts">
    <div class="contacts__row">
      <span class="contacts__item"><svg viewBox="0 0 24 24"><path d="M6.6 10.8a15 15 0 006.6 6.6l2.2-2.2c.3-.3.7-.4 1-.2 1.1.4 2.3.6 3.6.6.6 0 1 .4 1 1V20c0 .6-.4 1-1 1A17 17 0 013 4c0-.6.4-1 1-1h3.5c.6 0 1 .4 1 1 0 1.3.2 2.5.6 3.6.1.3 0 .7-.2 1z"/></svg>817-555-0142</span>
      <span class="contacts__item"><svg viewBox="0 0 24 24"><path d="M6 3h10v5H6zM4 9h16v9h-3v3H7v-3H4zm5 7v3h6v-3z"/></svg>817-555-0187</span>
      <span class="contacts__item"><svg viewBox="0 0 24 24"><path d="M3 5h18v14H3zm2 2v1l7 5 7-5V7l-7 5z"/></svg>daleharwick@vesnamail.net</span>
    </div>
    <div class="contacts__address">5817 Elmwood Crest Rd. Fort Worth, Texas 76243</div>
  </div>
</section>

<section class="card card--back-blue">
  <div class="wordmark"><span class="wordmark__square"></span>Dale Harwick Realtors</div>
</section>

<section class="card card--back-dark">
  <div class="wordmark"><span class="wordmark__square"></span>Dale Harwick Realtors</div>
  <div class="card__web-bottom">www.DaleHarwickRealtors.com</div>
</section>

<section class="card card--back-navy">
  <div class="wordmark"><span class="wordmark__square"></span>Dale Harwick Realtors</div>
  <div class="card__web-bottom">www.DaleHarwickRealtors.com</div>
</section>

</body>
</html>
```